Skyforge Solutions Inc. - new Website

1 - Take the existing content and elevate the site to be much more dynamic. www.skyforgenorth.example. We are looking for a site that is modern and easily updated. Aerospace is our primary industry but rail and engineering are part of who we are.

2- New logo to implement (attached)

3 - Remove customer access page

4 - website to be built so that we can change and update from our offices with no coding requirements.

5 - Pictures available

6 - Bilingual French and English

7 - News / Press page

8 - Social media icons link Twitter, youtube and linkedin

9 - add an PLOV engineering page (content will be added later) Plov logo attached

10 - Please use stock photos, and but will pay for royalty if necessary

Target Market(s)

Airlines 80%
Rail 10%
Other transportation 10%

Industry/Entity Type

Aviation

Number of Pages Required

5+ page

Font styles to use
Sans Serif

Requirements
Must have
• Skyforge logo
• Logo Plov (Plover Logistics Operations Venture inc.)
• Dynamic modern look and feel
• Existing content from our website and attched introduction document plus the above
• Press page
• Industry pictures - Repair (as per our website)
Nice to have
• Animation
• You tube links
• Blog
• Career page

```html
<!DOCTYPE html>
<html lang="en">
<head>
<meta charset="utf-8">
<title>Skyforge Solutions Inc.</title>
<link href="https://fonts.googleapis.com/css2?family=Montserrat:wght@400;600;700&family=Open+Sans:wght@400;600;700&display=swap" rel="stylesheet">
<style>
:root{
  --blue:#0a6aa6;
  --blue-dark:#08598c;
  --red:#e8202a;
  --ink:#222222;
  --text:#777777;
  --muted:#9a9a9a;
  --light:#f1f1f1;
  --line:#e3e3e3;
  --footer:#252122;
  --footer-bottom:#1b1819;
  --teal:#7fcfc4;
}
*{margin:0;padding:0;box-sizing:border-box}
html,body{width:1200px;height:3255px;overflow:hidden}
body{position:relative;background:#fff;font-family:"Open Sans",Arial,sans-serif;color:var(--ink)}
.abs{position:absolute}
h2.section-title{position:absolute;left:0;width:1200px;text-align:center;font-family:"Montserrat",Arial,sans-serif;font-weight:600;font-size:21px;color:var(--ink)}

/* header */
.site-header{position:absolute;top:0;left:0;width:1200px;height:113px;background:#fff}
.brand{position:absolute;left:156px;top:30px;display:flex;align-items:center;gap:12px}
.brand-mark{width:46px;height:46px;background:var(--blue)}
.brand-name{font-family:"Montserrat",Arial,sans-serif;font-weight:700;font-size:22px;color:var(--blue)}
.top-links{position:absolute;right:158px;top:20px;display:flex;gap:14px;font-size:11px;color:var(--muted)}
.top-links .flag{display:inline-block;width:12px;height:8px;background:#c9323b;border-top:3px solid #2c4c8c;margin-right:4px;vertical-align:middle}
.social{position:absolute;display:flex;gap:8px}
.social span{display:block;width:26px;height:26px;border:1px solid var(--blue)}
.site-header .social{left:790px;top:59px}
.staff-login{position:absolute;left:929px;top:59px;width:113px;height:30px;background:var(--red);color:#fff;font-family:"Montserrat",Arial,sans-serif;font-size:10px;font-weight:600;text-align:center;line-height:30px;letter-spacing:.5px}

.main-nav{position:absolute;top:113px;left:0;width:1200px;height:35px;background:var(--blue)}
.main-nav ul{list-style:none;display:flex;position:absolute;left:156px;top:0;height:35px;align-items:center;font-family:"Montserrat",Arial,sans-serif;font-size:12px;color:#fff}
.main-nav li{margin-right:26px}
.main-nav li.home{width:42px;height:26px;background:var(--blue-dark);border-bottom:2px solid #fff;margin-right:30px;display:flex;align-items:center;justify-content:center}

/* hero */
.hero{position:absolute;top:148px;left:0;width:1200px;height:442px;background:linear-gradient(180deg,#c4ccd3 0%,#8a959e 45%,#3d4246 80%,#2b2d2f 100%)}
.hero-title{position:absolute;top:162px;left:0;width:1200px;text-align:center;color:#fff;font-family:"Montserrat",Arial,sans-serif;font-size:27px;font-weight:600}
.hero-sub{position:absolute;top:198px;left:0;width:1200px;text-align:center;color:#fff;font-size:15px}
.hero-btn{position:absolute;top:240px;left:544px;width:112px;height:30px;border:1px solid #fff;background:rgba(0,0,0,.35);color:#fff;font-size:11px;text-align:center;line-height:28px}
.hero .arrow{position:absolute;top:212px}

/* services */
.card{position:absolute;top:694px;width:204px}
.card .photo{height:120px}
.card h3{margin-top:28px;font-size:12px;font-weight:600;color:var(--ink)}
.card p{margin-top:8px;font-size:10.5px;line-height:15px;color:var(--text)}
.read-more{position:absolute;font-size:10.5px;color:var(--blue)}
.read-more.active{color:var(--red)}

/* company band */
.company{position:absolute;top:1144px;left:0;width:1200px;height:316px}
.company .photo{position:absolute;left:0;top:0;width:599px;height:316px;background:linear-gradient(180deg,#c8d3dc 0%,#aab3ba 55%,#6e8763 85%,#5d7553 100%)}
.company .panel{position:absolute;left:599px;top:0;width:601px;height:316px;background:var(--blue);color:#fff;padding:58px 0 0 41px}
.company h3{font-family:"Montserrat",Arial,sans-serif;font-size:15px;font-weight:600;letter-spacing:.3px}
.company .lead{margin-top:8px;font-size:11.5px;font-weight:700;line-height:17px;width:400px}
.company .body{margin-top:15px;font-size:11px;line-height:16.5px;width:410px}
.company .btn{margin-top:22px;width:200px;height:32px;border:1px solid #fff;font-size:10.5px;font-weight:600;text-align:center;line-height:30px;letter-spacing:.4px}

/* values */
.values{position:absolute;top:1460px;left:0;width:1200px;height:287px;background:#fff;box-shadow:0 10px 14px rgba(0,0,0,.08)}
.value{position:absolute;top:0;width:300px;text-align:center}
.value .icon{margin:58px auto 0;width:98px;height:98px;border-radius:50%;border:1px solid #f19a9e;display:flex;align-items:center;justify-content:center}
.value .icon.filled{background:var(--red);border-color:var(--red)}
.value h3{margin-top:32px;font-size:13px;font-weight:600;color:var(--ink)}
.value p{margin:6px auto 0;width:220px;font-size:10.5px;line-height:15px;color:var(--text)}

/* gallery */
.gallery-item{position:absolute;top:1851px;width:204px;height:159px}
.gallery-item .caption{position:absolute;left:0;top:66px;width:204px;text-align:center;color:#fff;font-size:12px;line-height:17px}
.arrow-muted{position:absolute}

/* partners */
.partners{position:absolute;top:2068px;left:0;width:1200px;height:245px;background:var(--light)}
.partner{position:absolute;top:93px;width:165px;height:98px;background:#fff;display:flex;align-items:center;justify-content:center;font-family:"Montserrat",Arial,sans-serif;font-weight:700;font-size:14px;color:#4a5560;text-align:center}

/* blog & press */
.col-title{position:absolute;top:2366px;font-family:"Montserrat",Arial,sans-serif;font-size:20px;font-weight:600;color:var(--ink)}
.col-rule{position:absolute;top:2402px;width:358px;height:2px;background:var(--teal)}
.post{position:absolute;top:2437px;width:204px}
.post .photo{height:141px}
.post .meta{margin-top:30px;font-size:9.5px;color:var(--red)}
.post h4{margin-top:5px;font-size:10.5px;font-weight:700;line-height:14px;color:var(--ink)}
.post p{margin-top:8px;font-size:10px;line-height:14px;color:var(--text)}
.press-item{position:absolute;left:686px;width:358px;height:72px}
.date{position:absolute;left:0;top:0;width:50px;height:72px;text-align:center}
.date .month{height:24px;font-size:8.5px;color:var(--muted);line-height:24px;border:1px solid var(--line);border-bottom:none}
.date .day{height:48px;background:var(--blue);color:#fff;font-family:"Montserrat",Arial,sans-serif;font-size:30px;line-height:48px}
.press-item h4{position:absolute;left:78px;top:8px;font-size:10.5px;font-weight:600;color:var(--ink)}
.press-item h4.active{color:var(--red)}
.press-item p{position:absolute;left:78px;top:24px;width:275px;font-size:10px;line-height:14px;color:var(--text)}

/* footer */
.site-footer{position:absolute;top:2815px;left:0;width:1200px;height:368px;background:var(--footer);color:#bdbdbd}
.footer-brand{position:absolute;left:156px;top:58px;display:flex;align-items:center;gap:12px}
.footer-brand .brand-mark{background:#8a8a8a}
.footer-brand .brand-name{color:#cfcfcf}
.footer-rule{position:absolute;left:156px;top:158px;width:302px;height:1px;background:#444}
.follow{position:absolute;left:156px;top:189px;font-size:11px;color:#ddd}
.site-footer .social{left:156px;top:218px}
.site-footer .social span{border-color:#1e6ea3;background:#1c3142}
.quick{position:absolute;left:536px;top:52px;font-size:11px;line-height:20.8px;color:#a8a8a8}
.quick h5{font-size:11px;font-weight:600;color:#ddd;margin-bottom:2px}
.quick li{list-style:none}
.quick li.active{color:var(--red)}
.office{position:absolute;left:764px;top:52px;font-size:11px;line-height:15px;color:#a8a8a8;width:260px}
.office h5{font-size:11px;font-weight:600;color:#ddd}
.map{position:absolute;left:764px;top:104px;width:278px;height:163px;background:radial-gradient(ellipse at 60% 50%,#6a6a6a 0%,#4a4a4a 60%,var(--footer) 100%)}
.map-tag{position:absolute;left:790px;top:190px;background:#ddd;color:#333;font-size:8px;padding:3px 8px}
.call{position:absolute;left:764px;top:284px;font-size:16px;color:#ddd}
.mail{position:absolute;left:764px;top:305px;font-size:10.5px;color:#a8a8a8}
.footer-bottom{position:absolute;top:3183px;left:0;width:1200px;height:72px;background:var(--footer-bottom);color:#8a8a8a;font-size:10.5px}
.footer-bottom p{position:absolute;left:156px;top:29px}
.footer-bottom svg{position:absolute;left:1032px;top:28px}
</style>
</head>
<body>

<header class="site-header">
  <div class="brand"><div class="brand-mark"></div><div class="brand-name">Skyforge Solutions Inc.</div></div>
  <div class="top-links"><span>Quality Certificate</span><span>/</span><span>Career</span><span>/</span><span><i class="flag"></i>Eng ⌄</span></div>
  <div class="social" aria-label="Social media links"><span></span><span></span><span></span></div>
  <div class="staff-login">STAFF LOGIN</div>
</header>

<nav class="main-nav">
  <ul>
    <li class="home"><svg width="13" height="12" viewBox="0 0 13 12"><path d="M6.5 0L0 6h2v6h3.5V8h2v4H11V6h2z" fill="#fff"/></svg></li>
    <li>About Us ⌄</li><li>Service ⌄</li><li>Products</li><li>PLOV Engineering</li><li>Sales Presentation</li><li>Resources</li><li>Patners</li><li>Contact Us</li>
  </ul>
</nav>

<section class="hero" role="img" aria-label="Photo of a large airliner engine and landing gear on the runway">
  <svg class="arrow" style="left:98px" width="10" height="14" viewBox="0 0 10 14"><path d="M8 1L2 7l6 6" stroke="#fff" stroke-width="2" fill="none"/></svg>
  <svg class="arrow" style="left:1092px" width="10" height="14" viewBox="0 0 10 14"><path d="M2 1l6 6-6 6" stroke="#fff" stroke-width="2" fill="none"/></svg>
  <h1 class="hero-title">At Skyforge Services,</h1>
  <p class="hero-sub">we are committed to the highest quality of service and accountability.</p>
  <div class="hero-btn">Learn More</div>
</section>

<h2 class="section-title" style="top:638px">Services We offer</h2>
<svg class="arrow-muted" style="left:96px;top:820px" width="8" height="12" viewBox="0 0 8 12"><path d="M7 0L0 6l7 6z" fill="#c3c3c3"/></svg>
<svg class="arrow-muted" style="left:1094px;top:820px" width="8" height="12" viewBox="0 0 8 12"><path d="M1 0l7 6-7 6z" fill="var(--blue)"/></svg>

<article class="card" style="left:156px"><div class="photo" role="img" aria-label="Photo of a technician repairing aircraft seats" style="background:linear-gradient(135deg,#8a9a72,#4a5a6a)"></div><h3>Aircraft Seats</h3><p>Lorem Ipsum has been the industry's standard dummy text ever when an unknown printer took a galley of type.</p></article>
<article class="card" style="left:384px"><div class="photo" role="img" aria-label="Photo of an airliner parked at the gate" style="background:linear-gradient(180deg,#b9c3cc,#6b6f74)"></div><h3>Line Cabin Maintenance</h3><p>Lorem Ipsum has been the industry's standard dummy text ever when an unknown printer took a galley of type.</p></article>
<article class="card" style="left:612px"><div class="photo" role="img" aria-label="Photo of technicians servicing in-flight entertainment units" style="background:linear-gradient(135deg,#2f4f7a,#b3874a)"></div><h3>Bench IFE Maintenance</h3><p>Lorem Ipsum has been the industry's standard dummy text ever when an unknown printer took a galley of type.</p></article>
<article class="card" style="left:840px"><div class="photo" role="img" aria-label="Photo of cargo equipment on the apron beside an airliner" style="background:linear-gradient(180deg,#9fb3c8,#6d6f6c)"></div><h3>Cargo Equipment</h3><p>Lorem Ipsum has been the industry's standard dummy text ever when an unknown printer took a galley of type.</p></article>
<span class="read-more" style="left:156px;top:953px">Read More ...</span>
<span class="read-more active" style="left:384px;top:953px">Read More ...</span>
<span class="read-more" style="left:612px;top:953px">Read More ...</span>
<span class="read-more" style="left:840px;top:953px">Read More ...</span>

<h2 class="section-title" style="top:1066px">Why Skyforge Services, Inc.?</h2>

<section class="company">
  <div class="photo" role="img" aria-label="Photo of the modern glass company headquarters building"></div>
  <div class="panel">
    <h3>Company History</h3>
    <p class="lead">Founded in 1962 in Montreal, Canada as Ironkeel AeroMarine.</p>
    <p class="body">Skyforge Services will satisfy our customers' needs through the continuous development of innovative and cost-effective repair and service solutions. We will continue to provide the highest levels of customer service in the industry to the mutual reward of our customers and our employees ...</p>
    <div class="btn">DISCOVER MORE ABOUT US</div>
  </div>
</section>

<section class="values">
  <div class="value" style="left:145px">
    <div class="icon"><svg width="44" height="30" viewBox="0 0 44 30"><path d="M2 10l10-6 8 4 8-4 14 6M12 4l-6 14 12 8 4-2M32 4l6 14-10 8-4-2M16 14l6-4 8 8" stroke="var(--red)" stroke-width="2" fill="none" stroke-linejoin="round"/></svg></div>
    <h3>Bond of Trust</h3><p>Lorem Ipsum has been the industry's standard dummy text ever</p>
  </div>
  <div class="value" style="left:451px">
    <div class="icon filled"><svg width="40" height="40" viewBox="0 0 40 40"><circle cx="20" cy="20" r="12" stroke="#fff" stroke-width="2.5" fill="none"/><path d="M20 2v12M20 26v12M2 20h12M26 20h12" stroke="#fff" stroke-width="2.5"/></svg></div>
    <h3>Focus on Customer Service</h3><p>Lorem Ipsum has been the industry's standard dummy text ever</p>
  </div>
  <div class="value" style="left:751px">
    <div class="icon"><svg width="36" height="40" viewBox="0 0 36 40"><path d="M4 2h20l6 6v14M30 30v8H4V2" stroke="var(--red)" stroke-width="2" fill="none"/><path d="M9 12h14M9 18h14M9 24h8" stroke="var(--red)" stroke-width="2"/><circle cx="27" cy="30" r="7" fill="var(--red)"/><path d="M23.5 30l2.5 2.5 4.5-5" stroke="#fff" stroke-width="2" fill="none"/></svg></div>
    <h3>Quality &amp; Compliance</h3><p>Lorem Ipsum has been the industry's standard dummy text ever</p>
  </div>
</section>

<h2 class="section-title" style="top:1797px">Product Gallery</h2>
<svg class="arrow-muted" style="left:96px;top:1924px" width="8" height="12" viewBox="0 0 8 12"><path d="M7 0L0 6l7 6z" fill="#c3c3c3"/></svg>
<svg class="arrow-muted" style="left:1094px;top:1924px" width="8" height="12" viewBox="0 0 8 12"><path d="M1 0l7 6-7 6z" fill="#c3c3c3"/></svg>
<div class="gallery-item" style="left:156px;background:linear-gradient(180deg,#d8d2c8,#8a2a52)" role="img" aria-label="Photo of an aircraft cabin galley with curtains"></div>
<div class="gallery-item" style="left:384px;background:linear-gradient(180deg,#4f6f6a,#1f4a3c)" role="img" aria-label="Photo of green leather aircraft seat covers"><div class="caption">Leather &amp; E-leather<br>Covers</div></div>
<div class="gallery-item" style="left:612px;background:linear-gradient(180deg,#3d4147,#b8403a)" role="img" aria-label="Photo of red and grey aircraft seats"></div>
<div class="gallery-item" style="left:840px;background:linear-gradient(135deg,#6b4a2a,#d9b88a)" role="img" aria-label="Photo of tan leather business jet seats"></div>

<section class="partners">
  <h2 class="section-title" style="top:41px">Skyforge Customers &amp; Partners</h2>
  <svg class="arrow-muted" style="left:96px;top:137px" width="8" height="12" viewBox="0 0 8 12"><path d="M7 0L0 6l7 6z" fill="#c3c3c3"/></svg>
  <svg class="arrow-muted" style="left:1094px;top:137px" width="8" height="12" viewBox="0 0 8 12"><path d="M1 0l7 6-7 6z" fill="#c3c3c3"/></svg>
  <div class="partner" style="left:156px">Parcelwing</div>
  <div class="partner" style="left:336px">Aerolane</div>
  <div class="partner" style="left:516px">Jetmarch Airways</div>
  <div class="partner" style="left:696px">Northtrail Air</div>
  <div class="partner" style="left:877px">Harbour Field</div>
</section>

<h2 class="col-title" style="left:156px">Latest Blog</h2>
<div class="col-rule" style="left:156px"></div>
<h2 class="col-title" style="left:686px">Press Release</h2>
<div class="col-rule" style="left:686px"></div>

<article class="post" style="left:156px"><div class="photo" role="img" aria-label="Photo of ground crew working beside an aircraft engine" style="background:linear-gradient(180deg,#6d7e92,#2e3b4c)"></div><p class="meta">By Mara Ellison / Jun 12, 20143</p><h4>Skyforge starts providing services for Savanna Airways</h4><p>Lorem ipsum dolor sit amet, consectetur adipiscing elit. In pretium vulputate scelerisque ...</p></article>
<article class="post" style="left:384px"><div class="photo" role="img" aria-label="Photo of a technician in a high-visibility vest near an aircraft" style="background:linear-gradient(180deg,#3c4a58,#b07a2a)"></div><p class="meta">By Mara Ellison / Jun 12, 20143</p><h4>Skyforge starts servicing for Dunecrest Airways</h4><p>Lorem ipsum dolor sit amet, consectetur adipiscing elit. In pretium vulputate scelerisque ...</p></article>
<span class="read-more" style="left:156px;top:2744px">Read More ...</span>
<span class="read-more" style="left:384px;top:2744px">Read More ...</span>

<div class="press-item" style="top:2441px"><div class="date"><div class="month">AUG</div><div class="day">25</div></div><h4>Providing services for Savanna Airways</h4><p>Suspendisse faucibus sem nec dictum tristique morbi quis scelerisque ...</p></div>
<div class="press-item" style="top:2528px"><div class="date"><div class="month">SEP</div><div class="day">18</div></div><h4 class="active">1Y check for Lotus Air, Thailand</h4><p>Suspendisse faucibus sem nec dictum tristique morbi quis scelerisque ...</p></div>
<div class="press-item" style="top:2615px"><div class="date"><div class="month">JUL</div><div class="day">13</div></div><h4>To our valued customers</h4><p>Suspendisse faucibus sem nec dictum tristique morbi quis scelerisque ...</p></div>
<div class="press-item" style="top:2702px"><div class="date"><div class="month">SEP</div><div class="day">07</div></div><h4>Technical support for NKA, BQ and TRV</h4><p>Suspendisse faucibus sem nec dictum tristique morbi quis scelerisque ...</p></div>

<footer class="site-footer">
  <div class="footer-brand"><div class="brand-mark"></div><div class="brand-name">Skyforge Solutions Inc.</div></div>
  <div class="footer-rule"></div>
  <p class="follow">Follow Us:</p>
  <div class="social" aria-label="Social media links"><span></span><span></span><span></span></div>
  <div class="quick">
    <h5>Quick Links</h5>
    <ul><li>Home</li><li>About Us</li><li class="active">Service</li><li>Products</li><li>PLOV Engineering</li><li>Sales Presentation</li><li>Contact Us</li><li>Resources</li><li>Patners</li><li>Quality Certificate</li><li>Career</li><li>Contact Us</li></ul>
  </div>
  <div class="office"><h5>Corpporate Office</h5><p>42 Harrow Avenue Dorval, Quebec<br>Canada, H9P 1X4</p></div>
  <div class="map" role="img" aria-label="Map of Canada with office location pins"></div>
  <div class="map-tag">VANCOUVER</div>
  <p class="call">Call Us: (514) 555-0148</p>
  <p class="mail">info@skyforgenorth.example</p>
</footer>
<div class="footer-bottom">
  <p>© 2016 Skyforge Services, Inc. Unauthorized duplication is strictly prohibited.</p>
  <svg width="12" height="14" viewBox="0 0 12 14"><path d="M6 1v12M1 6l5-5 5 5" stroke="var(--blue)" stroke-width="2" fill="none"/></svg>
</div>

</body>
</html>
```